Car Spare Parts Packaging Box

I need a packaging design for car spare parts, specifically electrical parts or motor electric, such as fuel pump, motor power window, switch power window, motor fan radiator, sensor oxygen, starter, alternator, etc.

Our logo is as attached. Slogan "Premium Quality Auto Parts".
Font:
BinnerD (company name)
MictrogrammaDMedExt (slogan)

Color:
Blue - the gradients consist of C100 M100 Y0 K0 / C100 M0 Y0 K0
Yellow - gradients consist of C16 M32 Y100 K61 / C0 M0 Y100 K0

For reference:
KORVEL (multi products), Mirta (fuel pump, sensor oxygen), Votra (multi product)
Updates

Project Deadline Extended
Reason: Dear all, I still haven't find one suit my chemistry. Please browse existing worldwide brand from Japan and germany for more references. Since i am abroad at the moment, i will inform you more existing brand by tomorrow.

Project Deadline Extended
Reason: For some designers to finalize their work.

Industry/Entity Type

Electrical

Font styles to use
Serif
Sans Serif

Colors
0555a3
0892cd

Requirements
Must have
• 1. Space at one of the sides for label.
2. Gradient color design
3. Less white background.
Korvel n votra as main reference.
Nice to have
• wording: some of below options.
durable
reliable
high quality
best quality
quality guaranteed
replacement parts
long life
spare parts silhouette / blue print / real picture
Should not have
• 1. should not have car draw/picture, since we are selling car spare parts, not the car itself.
2. do not use common font: arial, times new roman.
Expect a new unique font.

```html
<!DOCTYPE html>
<html lang="en">
<head>
<meta charset="utf-8">
<title>Kestran Auto Parts – Packaging Panels</title>
<link rel="stylesheet" href="https://fonts.googleapis.com/css2?family=Michroma&family=Russo+One&family=Oswald:wght@500;600&family=Roboto:wght@400&display=swap">
<style>
  :root {
    --stage: #d9dadc;
    --blue-light: #0892cd;
    --blue-mid: #1f78c8;
    --blue-deep: #0555a3;
    --blue-violet: #2a3b96;
    --blue-night: #1d2a7a;
    --yellow: #ffd21c;
    --yellow-deep: #e2a90c;
    --ink: #141414;
    --white: #ffffff;
    --silver: #b9bec6;
  }
  * { box-sizing: border-box; margin: 0; padding: 0; }
  html, body { width: 1200px; height: 836px; overflow: hidden; }
  body {
    background: var(--stage);
    font-family: "Roboto", sans-serif;
    position: relative;
  }

  .panel {
    position: absolute;
    overflow: hidden;
    background: linear-gradient(160deg, var(--blue-light) 0%, var(--blue-mid) 45%, var(--blue-deep) 100%);
  }
  .facet { position: absolute; inset: 0; }
  .facet--light {
    background: linear-gradient(170deg, #3aa2e0 0%, var(--blue-mid) 100%);
    clip-path: polygon(0 0, 22% 0, 30% 100%, 0 100%);
    opacity: .55;
  }
  .facet--mid {
    background: linear-gradient(170deg, #2c63c0 0%, var(--blue-deep) 100%);
    clip-path: polygon(22% 0, 44% 0, 48% 100%, 30% 100%);
  }
  .facet--deep {
    background: linear-gradient(165deg, var(--blue-violet) 0%, var(--blue-night) 100%);
    clip-path: polygon(44% 0, 100% 0, 100% 100%, 64% 100%);
  }

  .brand {
    position: absolute;
    display: flex; align-items: center; gap: 8px;
  }
  .brand__mark {
    width: 34px; height: 34px;
    background: var(--yellow);
    flex: none;
  }
  .brand__text { display: flex; flex-direction: column; }
  .brand__name {
    font-family: "Russo One", sans-serif;
    font-size: 30px; line-height: 1;
    color: var(--white);
    letter-spacing: 1px;
  }
  .brand__slogan {
    font-family: "Michroma", sans-serif;
    font-size: 7.5px; color: var(--white);
    margin-top: 5px; letter-spacing: .2px;
  }

  .band {
    position: absolute; left: 0; right: 0;
    height: 64px;
    background: linear-gradient(180deg, var(--yellow) 0%, #f7c514 60%, var(--yellow-deep) 100%);
    border-top: 4px solid #6fb3ea;
    border-bottom: 4px solid #6fb3ea;
    display: flex; align-items: center;
    white-space: nowrap;
  }
  .band__name {
    font-family: "Russo One", sans-serif;
    font-size: 30px; color: var(--ink);
    letter-spacing: .5px;
  }

  .claims {
    position: absolute;
    text-align: right;
    font-family: "Michroma", sans-serif;
    font-size: 10px; line-height: 1.7;
    color: var(--white);
    white-space: nowrap;
  }

  .product-photo {
    position: absolute;
    border-radius: 50%;
    background: radial-gradient(circle at 45% 45%, #f2f3f5 0%, var(--silver) 55%, #5d636d 100%);
  }

  .label {
    position: absolute;
    background: var(--white);
    border-radius: 22px;
    text-align: center;
    color: var(--ink);
  }
  .label__title {
    font-family: "Oswald", sans-serif; font-weight: 600;
    font-size: 27px; margin-top: 18px;
  }
  .label__serial { font-size: 15px; margin-top: 6px; }
  .label__note { font-size: 15px; margin-top: 60px; }

  .alt-side  { left: 70px;  top: 50px;  width: 330px; height: 380px; }
  .alt-front { left: 400px; top: 50px;  width: 360px; height: 380px; }
  .st-front  { left: 440px; top: 460px; width: 380px; height: 320px; }
  .st-side   { left: 820px; top: 460px; width: 310px; height: 320px; }
</style>
</head>
<body>

  <section class="panel alt-side">
    <div class="brand" style="left:22px; top:28px;">
      <span class="brand__mark"></span>
      <span class="brand__text">
        <span class="brand__name">KESTRAN</span>
        <span class="brand__slogan">Premium Quality Auto Parts</span>
      </span>
    </div>
    <div class="band" style="top:165px;"></div>
    <div class="label" style="left:24px; top:120px; width:176px; height:230px;">
      <p class="label__title">ALTERNATOR</p>
      <p class="label__serial">SN: 5669-2982818</p>
      <p class="label__note">Lorem Ipsum lorem</p>
    </div>
  </section>

  <section class="panel alt-front">
    <div class="facet facet--light"></div>
    <div class="facet facet--mid"></div>
    <div class="facet facet--deep"></div>
    <div class="brand" style="left:160px; top:28px;">
      <span class="brand__mark"></span>
      <span class="brand__text">
        <span class="brand__name">KESTRAN</span>
        <span class="brand__slogan">Premium Quality Auto Parts</span>
      </span>
    </div>
    <div class="band" style="top:190px; right:148px; padding-left:12px;">
      <span class="band__name" style="font-size:28px;">Alternator</span>
    </div>
    <p class="claims" style="right:16px; top:188px;">replacement parts<br>durable &amp; relible<br>best quality</p>
    <div class="product-photo" role="img" aria-label="Photo of a car alternator" style="left:80px; top:270px; width:110px; height:100px;"></div>
  </section>

  <section class="panel st-front">
    <div class="facet facet--light"></div>
    <div class="facet facet--mid"></div>
    <div class="facet facet--deep"></div>
    <div class="brand" style="left:170px; top:26px;">
      <span class="brand__mark"></span>
      <span class="brand__text">
        <span class="brand__name">KESTRAN</span>
        <span class="brand__slogan">Premium Quality Auto Parts</span>
      </span>
    </div>
    <div class="band" style="top:120px; right:180px; padding-left:26px;">
      <span class="band__name">Starter</span>
    </div>
    <p class="claims" style="right:18px; top:118px;">replacement parts<br>durable &amp; relible<br>best quality</p>
    <div class="product-photo" role="img" aria-label="Photo of a car starter motor" style="left:150px; top:215px; width:130px; height:80px;"></div>
  </section>

  <section class="panel st-side" style="background:linear-gradient(165deg, var(--blue-violet) 0%, var(--blue-night) 100%);">
    <div class="brand" style="left:22px; top:26px;">
      <span class="brand__mark"></span>
      <span class="brand__text">
        <span class="brand__name">KESTRAN</span>
        <span class="brand__slogan">Premium Quality Auto Parts</span>
      </span>
    </div>
    <div class="band" style="top:120px; justify-content:flex-end; padding-right:30px;">
      <span class="band__name">Starter</span>
    </div>
  </section>

</body>
</html>
```